RKD Cattleworks needs Buisness Card design using new logo

We need a business card design that ties our website and our new logo together. www.rkdcattleworks-example.com The logo will be added to our website at a later date and replace the existing rkd cattleworks that is on the webpage. We are looking for a simple & professional design.

Target Market(s)

Cattle Producers, Ranchers

Industry/Entity Type

Agriculture

Contact Information for Business Card

Side one:
logo
www.rkdcattleworks-example.com

Side two:
RKD Cattleworks
Dennis & Marla Kovacs
Brindle Creek, MB Canada
(555) 316-2984/(555) 472-9051
kovacs47@ploverline-example.net

Font styles to use
Serif
Sans Serif
Script

Requirements
Must have
• We would like to tie our new logo in with our website on the business card.

```html
<!DOCTYPE html>
<html lang="en">
<head>
<meta charset="utf-8">
<title>RKD Cattleworks Business Card</title>
<link rel="stylesheet" href="https://fonts.googleapis.com/css2?family=Questrial&family=Source+Sans+3:ital,wght@0,400;0,600;1,400&display=swap">
<style>
  :root {
    --page-bg: #ffffff;
    --card-dark: #231f20;
    --card-light: #ffffff;
    --ink-white: #ffffff;
    --ink-grey: #3d3d3f;
    --ink-teal: #1c3c45;
    --ink-body: #2b2b2b;
    --accent-red: #c8402e;
    --rule-orange: #e8957a;
    --card-edge: #e4e4e4;
  }
  * { margin: 0; padding: 0; box-sizing: border-box; }
  html, body {
    width: 965px; height: 1200px; overflow: hidden;
    background: var(--page-bg);
  }
  .canvas { position: relative; width: 965px; height: 1200px; }
  .card {
    position: absolute; left: 128px; width: 707px; height: 403px;
  }
  .card--front { top: 134px; background: var(--card-dark); }
  .card--back { top: 608px; background: var(--card-light); border: 1px solid var(--card-edge); }

  .front-brand {
    position: absolute; left: 0; right: 0; top: 160px;
    text-align: center;
    font-family: "Questrial", sans-serif;
    font-size: 50px; color: var(--ink-white);
  }
  .front-web {
    position: absolute; left: 0; right: 0; top: 358px;
    text-align: center;
    font-family: "Source Sans 3", sans-serif; font-weight: 600;
    font-size: 16px; letter-spacing: 4px; color: var(--accent-red);
  }

  .back-brand {
    position: absolute; left: 61px; top: 120px;
    font-family: "Questrial", sans-serif;
    font-size: 38px; color: var(--ink-grey);
  }
  .holder-name {
    position: absolute; right: 66px; top: 192px;
    font-family: "Source Sans 3", sans-serif; font-weight: 600;
    font-size: 28px; color: var(--ink-teal);
  }
  .divider {
    position: absolute; left: 61px; width: 582px; top: 241px;
    height: 1.5px; background: var(--rule-orange);
  }
  .location {
    position: absolute; right: 66px; top: 248px;
    font-family: "Source Sans 3", sans-serif; font-style: italic;
    font-size: 15px; color: var(--ink-body);
  }
  .contact {
    position: absolute; display: flex; align-items: center; gap: 12px;
    font-family: "Source Sans 3", sans-serif;
    font-size: 15.5px; letter-spacing: 0.8px; color: var(--ink-body);
  }
  .contact svg { width: 16px; height: 16px; flex: none; }
  .contact--phone1 { left: 201px; top: 296px; }
  .contact--phone2 { left: 201px; top: 327px; }
  .contact--email { left: 421px; top: 296px; letter-spacing: 0.3px; }
  .contact--web { left: 421px; top: 327px; letter-spacing: 0.3px; }
</style>
</head>
<body>
<main class="canvas">
  <section class="card card--front" aria-label="Card front">
    <div class="front-brand">RKD Cattleworks</div>
    <div class="front-web">www.rkdcattleworks-example.com</div>
  </section>

  <section class="card card--back" aria-label="Card back">
    <div class="back-brand">RKD Cattleworks</div>
    <div class="holder-name">Dennis &amp; Marla Kovacs</div>
    <div class="divider"></div>
    <div class="location">Brindle Creek, MB Canada</div>

    <div class="contact contact--phone1">
      <svg viewBox="0 0 16 16" aria-hidden="true"><rect x="4" y="1" width="8" height="14" rx="2" fill="var(--accent-red)"/><rect x="5.5" y="3" width="5" height="5" fill="#fff"/></svg>
      <span>(555) 316-2984</span>
    </div>
    <div class="contact contact--phone2">
      <svg viewBox="0 0 16 16" aria-hidden="true"><rect x="4" y="1" width="8" height="14" rx="2" fill="var(--accent-red)"/><rect x="5.5" y="3" width="5" height="5" fill="#fff"/></svg>
      <span>(555) 472-9051</span>
    </div>
    <div class="contact contact--email">
      <svg viewBox="0 0 16 16" aria-hidden="true"><circle cx="8" cy="8" r="6.5" fill="none" stroke="var(--accent-red)" stroke-width="1.6"/><ellipse cx="8" cy="8" rx="2.8" ry="6.5" fill="none" stroke="var(--accent-red)" stroke-width="1.2"/><line x1="1.5" y1="8" x2="14.5" y2="8" stroke="var(--accent-red)" stroke-width="1.2"/></svg>
      <span>kovacs47@ploverline-example.net</span>
    </div>
    <div class="contact contact--web">
      <svg viewBox="0 0 16 16" aria-hidden="true"><rect x="1.5" y="3.5" width="13" height="9" fill="none" stroke="var(--accent-red)" stroke-width="1.5"/><polyline points="1.5,3.5 8,9 14.5,3.5" fill="none" stroke="var(--accent-red)" stroke-width="1.5"/></svg>
      <span>www.rkdcattleworks-example.com</span>
    </div>
  </section>
</main>
</body>
</html>
```